Beauty Packaging Design for small bottle

Design label to have a similar look and feel as other products (as attached for reference). This will be a printed on a gold metallic label, so although the design should be in gold to show us how it will eventually look, the final file will need to have the gold areas in red.

All project information is outline in the attached brief. Please contact us for any questions along the way.

Target Market(s)

Educated, savvy women 30-65 yrs old.

Industry/Entity Type

Hair And Beauty

Font styles to use
Other font styles liked:
• See brief

Requirements
Must have
• See brief
• Color(s): black, gold, white
Nice to have
• purple (CMYK 33/55/0/51)
Should not have
• See brief

```html
<!DOCTYPE html>
<html lang="en">
<head>
<meta charset="utf-8">
<title>Solenne Retinol Prime – Label</title>
<link href="https://fonts.googleapis.com/css2?family=Cinzel:wght@400;600;700&family=Great+Vibes&display=swap" rel="stylesheet">
<style>
  :root {
    --bg: #f4f4f4;
    --label-black: #161616;
    --label-edge: #0b0b0b;
    --pattern-tone: #262626;
    --gold: #d8b54a;
    --gold-light: #f1d77c;
    --gold-deep: #9a7424;
    --white: #f5f5f2;
  }
  html, body {
    margin: 0;
    padding: 0;
    width: 1200px;
    height: 854px;
    overflow: hidden;
    background: var(--bg);
  }
  .canvas {
    position: relative;
    width: 1200px;
    height: 854px;
    background: radial-gradient(ellipse at center, #ffffff 0%, var(--bg) 75%);
  }
  .label {
    position: absolute;
    left: 240px;
    top: 167px;
    width: 720px;
    height: 520px;
    background: linear-gradient(180deg, #1d1d1d 0%, var(--label-black) 60%, var(--label-edge) 100%);
    overflow: hidden;
  }
  .label__pattern {
    position: absolute;
    inset: 0;
    background: radial-gradient(ellipse at 50% 40%, var(--pattern-tone) 0%, rgba(22,22,22,0) 70%);
  }
  .label__ornament {
    position: absolute;
    left: 29px;
    top: 114px;
    width: 209px;
    height: 349px;
    border-radius: 6px;
    background: linear-gradient(160deg, rgba(241,215,124,0.55) 0%, rgba(216,181,74,0.4) 50%, rgba(154,116,36,0.3) 100%);
  }
  .brand {
    position: absolute;
    top: 80px;
    left: 0;
    width: 100%;
    display: flex;
    justify-content: center;
    align-items: center;
    gap: 14px;
  }
  .brand__mark {
    width: 50px;
    height: 50px;
    border-radius: 50%;
    background: var(--gold);
  }
  .brand__name {
    font-family: "Cinzel", serif;
    font-weight: 600;
    font-size: 56px;
    letter-spacing: 3px;
    color: var(--gold);
    line-height: 1;
    border-bottom: 3px solid var(--gold);
    padding-bottom: 4px;
  }
  .product__name {
    position: absolute;
    left: 110px;
    top: 178px;
    width: 510px;
    margin: 0;
    text-align: center;
    font-family: "Cinzel", serif;
    font-weight: 700;
    font-size: 96px;
    color: var(--white);
    line-height: 1;
  }
  .product__variant {
    position: absolute;
    left: 281px;
    top: 280px;
    font-family: "Great Vibes", cursive;
    font-size: 92px;
    color: var(--white);
    line-height: 1;
  }
  .claim {
    position: absolute;
    left: 108px;
    top: 395px;
    width: 497px;
    height: 42px;
    box-sizing: border-box;
    border: 2px solid var(--gold);
    display: flex;
    align-items: center;
    justify-content: center;
    font-family: "Cinzel", serif;
    font-weight: 700;
    font-size: 21px;
    color: var(--white);
    background: var(--label-edge);
  }
  .ingredients {
    position: absolute;
    left: 108px;
    top: 446px;
    width: 497px;
    text-align: center;
    font-family: "Cinzel", serif;
    font-weight: 600;
    font-size: 16px;
    letter-spacing: 1px;
    color: var(--white);
  }
</style>
</head>
<body>
  <main class="canvas">
    <section class="label">
      <div class="label__pattern" role="img" aria-label="Faint dark hexagonal line pattern across the label"></div>
      <div class="label__ornament" role="img" aria-label="Large gold geometric ornament"></div>

      <div class="brand">
        <span class="brand__mark"></span>
        <span class="brand__name">SOLENNE</span>
      </div>

      <h1 class="product__name">RETINOL</h1>
      <span class="product__variant">Prime</span>

      <div class="claim">Intensive Overnight Moisturizer</div>
      <div class="ingredients">With Hyaluronic Acid &amp; Aloe Vera</div>
    </section>
  </main>
</body>
</html>
```